Baby Boutique Needs a Business Card Design

We need a modern double sided business card design using the attached logo for Lil' Tot Nook.

Lil' Tot Nook is a baby boutique which sells only handmade clothing and accessories for both boys and girls. Our store will live exclusively online.

We would like to only use the colors that have been used in the logo.

Target Market(s)

Potential wholesale clients, Small business owners

Industry/Entity Type

Retail

Contact Information for Business Card

Name Wendell J. Ferris (Owner)
Email sales@ltotnook.com
Main Phone 787-203-6159
Cell phone 787-203-6742
Website www.LTotNook.com

Font styles to use
Sans Serif

Colors

Designer to choose colors to be used in the design.

Requirements
Must have
• -Would like to have icons that indentify the contact information.
• -Include our website
• -Include our tagline in a small area near the bottom. "Handmade Baby Creations"
• -Would like to include Facebook and Instagram Icons
• -
Nice to have
• Would like to have a simple back side with the logo.
• Something along the lines of the harbor ledger card attached.

```html
<!DOCTYPE html>
<html lang="en">
<head>
<meta charset="utf-8">
<title>Lil' Tot Nook – Business Card</title>
<link rel="stylesheet" href="https://fonts.googleapis.com/css2?family=Roboto:wght@400;500&display=swap">
<style>
  :root {
    --backdrop: #ebebeb;
    --card-black: #141414;
    --card-white: #ffffff;
    --teal: #78c8b9;
    --coral: #e8595a;
    --ink: #1e1e1e;
    --paper-text: #f2f2f2;
  }
  * { margin: 0; padding: 0; box-sizing: border-box; }
  html, body { width: 1200px; height: 900px; overflow: hidden; }
  body {
    background: var(--backdrop);
    font-family: "Roboto", Arial, sans-serif;
    position: relative;
  }
  .card {
    position: absolute;
    top: 295px;
    width: 540px;
    height: 310px;
    border-radius: 24px;
    overflow: hidden;
    box-shadow: 0 14px 30px rgba(0,0,0,0.18);
  }
  .card-back {
    left: 40px;
    background: radial-gradient(ellipse at 50% 40%, #262626 0%, var(--card-black) 70%);
  }
  .card-front { left: 620px; background: var(--card-white); }

  .brand-name {
    font-family: "Roboto", Arial, sans-serif;
    font-weight: 500;
    color: var(--teal);
    white-space: nowrap;
    position: absolute;
    text-align: center;
  }
  .card-back .brand-name {
    left: 0; right: 0; top: 110px;
    font-size: 54px;
  }
  .social-row {
    position: absolute;
    left: 0; right: 0; top: 228px;
    display: flex;
    justify-content: center;
    gap: 10px;
  }
  .social-dot {
    width: 18px; height: 18px;
    border-radius: 50%;
    background: var(--coral);
  }

  .front-art { position: absolute; inset: 0; }
  .card-front .brand-name {
    left: 20px; width: 240px; top: 118px;
    font-size: 38px;
  }
  .holder {
    position: absolute;
    left: 365px; top: 60px;
  }
  .holder-name { color: var(--coral); font-size: 16px; font-weight: 500; }
  .holder-role { color: var(--teal); font-size: 12px; margin-top: 4px; }
  .contact-list {
    position: absolute;
    left: 365px; top: 132px;
    list-style: none;
  }
  .contact-item {
    display: flex;
    align-items: center;
    gap: 8px;
    height: 24px;
    color: var(--teal);
    font-size: 12.5px;
  }
  .contact-icon { width: 15px; height: 15px; flex: none; }
</style>
</head>
<body>

<section class="card card-back" aria-label="Card back">
  <div class="brand-name">Lil' Tot Nook</div>
  <div class="social-row">
    <span class="social-dot" aria-label="Social page"></span>
    <span class="social-dot" aria-label="Social page"></span>
  </div>
</section>

<section class="card card-front" aria-label="Card front">
  <svg class="front-art" viewBox="0 0 540 310" width="540" height="310">
    <defs>
      <clipPath id="dark-zone">
        <path d="M300,0 C292,120 265,230 205,310 L540,310 L540,0 Z"/>
      </clipPath>
      <clipPath id="light-zone">
        <path d="M0,0 L300,0 C292,120 265,230 205,310 L0,310 Z"/>
      </clipPath>
      <radialGradient id="dark-fill" cx="0.6" cy="0.45" r="0.7">
        <stop offset="0" stop-color="#262626"/>
        <stop offset="1" stop-color="#141414"/>
      </radialGradient>
    </defs>
    <path d="M300,0 C292,120 265,230 205,310 L540,310 L540,0 Z" fill="url(#dark-fill)"/>
    <path d="M248,0 L291,0 C284,100 266,180 232,250 C256,170 262,85 248,0 Z" fill="var(--teal)"/>
    <g font-family="Roboto, Arial, sans-serif" font-size="11" letter-spacing="10.5">
      <text x="85" y="284" fill="var(--ink)" clip-path="url(#light-zone)">Handmade Baby Creations</text>
      <text x="85" y="284" fill="var(--paper-text)" clip-path="url(#dark-zone)">Handmade Baby Creations</text>
    </g>
  </svg>

  <div class="brand-name">Lil' Tot Nook</div>

  <div class="holder">
    <div class="holder-name">Wendell J. Ferris</div>
    <div class="holder-role">Owner</div>
  </div>

  <ul class="contact-list">
    <li class="contact-item">
      <svg class="contact-icon" viewBox="0 0 16 16"><circle cx="8" cy="8" r="8" fill="var(--coral)"/><path d="M5.2,4.2 l1.6,0 l0.6,2 l-1,0.8 a5,5 0 0 0 2.6,2.6 l0.8,-1 l2,0.6 l0,1.6 a1,1 0 0 1 -1,1 a7,7 0 0 1 -6.6,-6.6 a1,1 0 0 1 1,-1 z" fill="#fff"/></svg>
      787-203-6159
    </li>
    <li class="contact-item">
      <svg class="contact-icon" viewBox="0 0 16 16"><circle cx="8" cy="8" r="8" fill="var(--coral)"/><rect x="5.5" y="3.5" width="5" height="9" rx="1" fill="none" stroke="#fff" stroke-width="1.2"/><circle cx="8" cy="11" r="0.6" fill="#fff"/></svg>
      787-203-6742
    </li>
    <li class="contact-item">
      <svg class="contact-icon" viewBox="0 0 16 16"><circle cx="8" cy="8" r="8" fill="var(--coral)"/><rect x="4" y="5" width="8" height="6" fill="#fff"/><path d="M4,5 L8,8.5 L12,5" fill="none" stroke="var(--coral)" stroke-width="1"/></svg>
      sales@ltotnook.com
    </li>
    <li class="contact-item">
      <svg class="contact-icon" viewBox="0 0 16 16"><circle cx="8" cy="8" r="8" fill="var(--coral)"/><g fill="none" stroke="#fff" stroke-width="1"><circle cx="8" cy="8" r="4.2"/><ellipse cx="8" cy="8" rx="1.8" ry="4.2"/><line x1="3.8" y1="8" x2="12.2" y2="8"/></g></svg>
      www.LTotNook.com
    </li>
  </ul>
</section>

</body>
</html>
```